Construction Company Business Card

Business Card Design using new Logo

Contact Information for Business Card

include all company info and website

Requirements
Must have
• Wesley Corman - President
ph. 254-617-0382
Cedar Knoll, TX
wesley@ironmarkframing.com
www.ironmarkframing.com

```html
<!DOCTYPE html>
<html lang="en">
<head>
<meta charset="UTF-8">
<title>Ironmark Framing — Business Card</title>
<link href="https://fonts.googleapis.com/css2?family=Poppins:wght@400;500;600&display=swap" rel="stylesheet">
<style>
  :root {
    --backdrop: #1c1c1c;
    --card-dark: #2a2a2a;
    --card-light: #ffffff;
    --accent-red: #c8262b;
    --ink: #333333;
    --logo-grey: #b9bcc2;
    --divider: #a3a3a3;
  }
  * { margin: 0; padding: 0; box-sizing: border-box; }
  html, body {
    width: 1200px; height: 1200px; overflow: hidden;
    background: var(--backdrop);
    font-family: "Poppins", sans-serif;
  }
  .stage {
    position: relative; width: 1200px; height: 1200px;
    display: flex; flex-direction: column; align-items: center; justify-content: center; gap: 70px;
  }
  .card {
    width: 840px; height: 480px; border-radius: 22px;
    position: relative; overflow: hidden;
  }
  .card--back {
    background: var(--card-dark);
    display: flex; align-items: center; justify-content: center;
  }
  .card--front {
    background: var(--card-light);
    display: flex; align-items: center;
    padding: 0 40px 0 50px;
  }
  .brand {
    display: flex; align-items: center; gap: 12px;
    font-weight: 500; text-transform: uppercase; white-space: nowrap;
  }
  .brand__mark { width: 14px; height: 14px; background: var(--accent-red); flex: 0 0 14px; }
  .card--back .brand { font-size: 34px; letter-spacing: 4px; color: #d9d9d9; }
  .card--front .brand { font-size: 23px; letter-spacing: 3px; color: var(--logo-grey); }
  .front__logo { flex: 0 0 340px; display: flex; justify-content: center; }
  .front__divider {
    flex: 0 0 2px; width: 2px; height: 200px; background: var(--divider); margin: 0 34px 0 28px;
  }
  .contact { flex: 1 1 auto; min-width: 0; }
  .contact__name {
    font-size: 24px; font-weight: 600; color: var(--ink);
    letter-spacing: 1.5px; text-transform: uppercase; line-height: 1.15; white-space: nowrap;
  }
  .contact__title {
    font-size: 19px; font-weight: 500; color: var(--accent-red);
    letter-spacing: 1.5px; text-transform: uppercase; margin-bottom: 14px;
  }
  .contact__list { list-style: none; }
  .contact__item {
    display: flex; align-items: center; gap: 10px;
    font-size: 18px; color: var(--ink); line-height: 1.6; white-space: nowrap;
  }
  .contact__icon { width: 18px; height: 18px; flex: 0 0 18px; fill: var(--accent-red); }
  .contact__icon--line { fill: none; stroke: var(--accent-red); stroke-width: 1.8; }
</style>
</head>
<body>
<main class="stage">
  <section class="card card--back" aria-label="Card back">
    <div class="brand"><span class="brand__mark"></span>Ironmark Framing</div>
  </section>

  <section class="card card--front" aria-label="Card front">
    <div class="front__logo">
      <div class="brand"><span class="brand__mark"></span>Ironmark Framing</div>
    </div>
    <div class="front__divider"></div>
    <div class="contact">
      <p class="contact__name">Wesley Corman</p>
      <p class="contact__title">President</p>
      <ul class="contact__list">
        <li class="contact__item">
          <svg class="contact__icon" viewBox="0 0 24 24"><path d="M6.6 10.8a15 15 0 0 0 6.6 6.6l2.2-2.2c.3-.3.7-.4 1-.2 1.1.4 2.3.6 3.6.6.6 0 1 .4 1 1V20c0 .6-.4 1-1 1A17 17 0 0 1 3 4c0-.6.4-1 1-1h3.5c.6 0 1 .4 1 1 0 1.3.2 2.5.6 3.6.1.3 0 .7-.2 1z"/></svg>
          254-617-0382
        </li>
        <li class="contact__item">
          <svg class="contact__icon" viewBox="0 0 24 24"><path d="M2 5h20v14H2z"/><path d="M3 6l9 7 9-7" fill="none" stroke="#fff" stroke-width="1.6"/></svg>
          wesley@ironmarkframing.com
        </li>
        <li class="contact__item">
          <svg class="contact__icon contact__icon--line" viewBox="0 0 24 24"><circle cx="12" cy="12" r="9"/><ellipse cx="12" cy="12" rx="4" ry="9"/><path d="M3 12h18M5 7h14M5 17h14"/></svg>
          www.ironmarkframing.com
        </li>
        <li class="contact__item">
          <svg class="contact__icon" viewBox="0 0 24 24"><path d="M12 2a7 7 0 0 0-7 7c0 5 7 13 7 13s7-8 7-13a7 7 0 0 0-7-7zm0 9.5A2.5 2.5 0 1 1 12 6.5a2.5 2.5 0 0 1 0 5z"/></svg>
          Cedar Knoll, TX
        </li>
      </ul>
    </div>
  </section>
</main>
</body>
</html>
```